依頼概要
初めまして。本書は、会社等の会議を実施する立場の人に向けてのものと
なっております。
■依頼の目的/概要
lumora出版、ビジネスパーソン向け書籍の表紙デザインをお願いします。
今のところ、題名は
「だれでも週末から家庭菜園がはかどる」

■本の内容
会社等で、会議をうまく進めていきたいがなかなか思うように
薦められない方向けに、誰でも簡単にこれだけのことを実践すれば
会議が上手く進められるというポイントをまとめたものになっております。

■デザイン要望
ビジネスパーソン向けですが、会議等に不慣れな方向けで
あまり難しく考えなくても、誰でも簡単にトライできるという
イメージを持ってもらえるようにしたいです。

現在、原稿は9割がたできております。添付ファイルをご参照ください。

その他何かご不明な点がございましたら、お気軽にご質問下さい。
よろしくお願いいたします。
名前は、ペンネームにする予定です。
今のところ、柚木 瑛之助が候補です。
■ 選んだ理由

私のイメージする会社内での和気あいあいとした雰囲気のイラストがまずは
気に入りました。
ターゲットが、会議がうまくできない人向けなので、なるべくそれを意識して
親しみやすいものを選びました。

■ 提案者全員のお礼・コメント

今回は、ターゲットが初心者向けであったので、親しみやすいものを選びましたが、
例えば、会議を上から見たイラストなどは、斬新なアイデアで印象深く
ターゲットが違えば、選んでいたと思います。
中身を理解して、提案いただけた方も多く、感謝いたします。
今後も、このシリーズを出版していきたいと考えておりますので
次の機会もよろしくお願いいたします。
ありがとうございました。

```html
<!DOCTYPE html>
<html lang="ja">
<head>
<meta charset="utf-8">
<title>だれでも週末から家庭菜園がはかどる</title>
<link rel="stylesheet" href="https://fonts.googleapis.com/css2?family=Noto+Sans+JP:wght@900&display=swap">
<style>
  :root {
    --paper: #ffffff;
    --ink: #111111;
    --ring: #ff2bf2;
    --glyph-size: 160px;
  }
  html, body {
    margin: 0;
    padding: 0;
    width: 750px;
    height: 1200px;
    overflow: hidden;
    background: var(--paper);
  }
  .cover {
    position: relative;
    width: 750px;
    height: 1200px;
    background: var(--paper);
    font-family: "Noto Sans JP", sans-serif;
    font-weight: 900;
    color: var(--ink);
  }
  .cover__ring {
    position: absolute;
    left: 0;
    top: 0;
    width: 750px;
    height: 1200px;
  }
  .cover__title {
    margin: 0;
    font-size: var(--glyph-size);
    font-weight: 900;
    line-height: 1;
  }
  .glyph {
    position: absolute;
    display: block;
    width: 170px;
    height: 170px;
    line-height: 170px;
    text-align: center;
  }
  .cover__author {
    position: absolute;
    left: 8px;
    top: 190px;
    margin: 0;
    font-size: 100px;
    line-height: 1;
    letter-spacing: 2px;
    white-space: nowrap;
  }
</style>
</head>
<body>
  <main class="cover">
    <svg class="cover__ring" viewBox="0 0 750 1200" aria-hidden="true">
      <circle cx="372" cy="522" r="238" fill="none" stroke="var(--ring)" stroke-width="130"/>
    </svg>

    <h1 class="cover__title" aria-label="だれでも週末から家庭菜園がはかどる">
      <!-- top row -->
      <span class="glyph" style="left:4px;top:0px">だ</span>
      <span class="glyph" style="left:190px;top:0px">れ</span>
      <span class="glyph" style="left:375px;top:0px">で</span>
      <span class="glyph" style="left:565px;top:0px">も</span>
      <!-- right column -->
      <span class="glyph" style="left:565px;top:175px">週</span>
      <span class="glyph" style="left:565px;top:345px">末</span>
      <span class="glyph" style="left:565px;top:515px">か</span>
      <span class="glyph" style="left:565px;top:685px">ら</span>
      <!-- bottom row, right to left -->
      <span class="glyph" style="left:565px;top:995px">家</span>
      <span class="glyph" style="left:375px;top:995px">庭</span>
      <span class="glyph" style="left:190px;top:995px">菜</span>
      <span class="glyph" style="left:4px;top:995px">園</span>
      <!-- left column, upward -->
      <span class="glyph" style="left:4px;top:805px">が</span>
      <span class="glyph" style="left:4px;top:610px">は</span>
      <span class="glyph" style="left:4px;top:415px">か</span>
      <!-- middle row -->
      <span class="glyph" style="left:230px;top:380px">ど</span>
      <span class="glyph" style="left:400px;top:370px">る</span>
    </h1>

    <p class="cover__author">柚木瑛之助</p>
  </main>
</body>
</html>
```